Purovane - A range of environmental public toilet products

We need a design for an existing company with a new direction. We supply toilet cleaning products, matts etc that not only keep your public toilet clean and smelling good but also clean pipes and toilet bowls at the same time.
Many of the products contain a unique enzyme deodorant formulation, which can effectively kill bacterial, deodorize, eliminating smells and clean the Urinal and pipes with every flush.

The web page needs to say we are clean and sparkeling but please note "THIS IS NOT A HOME PRODUCT but for public urinals and bathrooms.
Our product is not expensive but is helping the environment and
completely safe

Reason: Unfortunately all members of the comapny are still on holiday and I have not been able to contact 2 of them regarding the site and I would like their input. I think they are all back shortly but not sure.

Target Market(s)

Industrial Cleaners and suppliers to hotels, clubs etc

Industry/Entity Type

Environment

Requirements
Must have
• The front page will have:
Point of Difference
Products
Ordering
Testominials
FAQ
Our Policies
Contact Us
Nice to have
• Make it look like you would want to use the piublic toilets.
As you know public toilets can be ugly places/

```html
<!DOCTYPE html>
<html lang="en">
<head>
<meta charset="utf-8">
<title>Purovane – Public Washroom Products</title>
<link href="https://fonts.googleapis.com/css2?family=Source+Sans+3:ital,wght@0,400;0,600;0,700;1,400;1,600&family=PT+Sans+Narrow:wght@400;700&display=swap" rel="stylesheet">
<style>
:root{
  --page:#e6e6e6;
  --panel:#f4f4f4;
  --white:#ffffff;
  --orange:#f39a1e;
  --orange-deep:#e2620a;
  --orange-light:#f7b445;
  --blue:#1c4f9c;
  --blue-dark:#163f82;
  --grey-text:#4a4a4a;
  --grey-soft:#a9a9a9;
  --line:#dcdcdc;
  --badge-green:#8fcf4f;
  --badge-teal:#1d6a48;
  --badge-gold:#e9b12c;
}
*{margin:0;padding:0;box-sizing:border-box}
html,body{width:1104px;height:1200px;overflow:hidden;background:var(--page)}
body{font-family:"Source Sans 3",sans-serif;color:var(--grey-text);position:relative}
.abs{position:absolute}

.brand{left:92px;top:26px;display:flex;align-items:center;gap:10px}
.brand-name{font-size:50px;font-weight:700;color:var(--blue);letter-spacing:1px;line-height:1}
.brand-dot{width:12px;height:12px;border-radius:50%;background:var(--orange);margin-top:26px}

.contact{right:96px;top:34px;text-align:right;font-weight:600}
.contact-line{font-size:28px;letter-spacing:-1px;color:var(--grey-soft);line-height:1}
.contact-line b{color:var(--orange);font-weight:600}
.contact-mail{font-size:16px;color:var(--orange);margin-top:6px}

.frame{left:75px;top:113px;width:952px;height:1023px;background:var(--panel);border-radius:10px}

.nav{left:95px;top:133px;width:914px;height:57px;border-radius:4px;
  background:linear-gradient(#f9c05a,var(--orange));display:flex;align-items:center;padding-left:27px}
.nav a{font-family:"PT Sans Narrow",sans-serif;font-size:19px;color:#5a2e00;text-decoration:none;margin-right:32px;text-transform:uppercase}
.order-btn{left:824px;top:142px;width:176px;height:40px;border-radius:4px;background:linear-gradient(#3f7cd0,var(--blue-dark));
  color:#fff;font-family:"PT Sans Narrow",sans-serif;font-size:21px;display:flex;align-items:center;justify-content:flex-end;padding-right:14px}
.order-btn svg{position:absolute;left:8px;top:-10px}

.hero{left:97px;top:212px;width:718px;height:402px;border-radius:3px;overflow:hidden;
  background:radial-gradient(ellipse at 78% 55%,#ffffff 0%,#f0f0f0 40%,#d9d9d9 100%)}
.hero-copy{left:28px;top:25px;width:330px;font-style:italic;font-size:15.5px;line-height:25.6px;color:#3b3b3b;text-align:justify;letter-spacing:-0.2px}
.hero-copy .b{font-style:normal;font-weight:700;color:var(--blue)}
.hero-copy .o{font-style:normal;font-weight:700;color:var(--orange)}
.hero-fruit{left:32px;top:300px;width:96px;height:96px;border-radius:50%;background:radial-gradient(#ffe35a,#f2b200)}
.hero-scent{left:46px;top:268px;font-style:italic;font-size:20px;color:var(--blue)}
.hero-tag1{left:142px;top:306px;font-size:24px;font-weight:700;color:var(--orange);letter-spacing:-0.5px}
.hero-tag2{left:140px;top:332px;font-size:33px;font-weight:700;color:var(--blue);letter-spacing:-1px}
.hero-product{left:505px;top:258px;width:115px;height:90px;border-radius:50%;background:radial-gradient(#e2ef6a,#b8cf2a)}

.points{left:838px;top:222px;width:166px;list-style:none}
.points li{font-style:italic;font-weight:600;font-size:15px;letter-spacing:-0.4px;color:var(--blue);line-height:21px;padding:0 0 10px;border-bottom:1px solid var(--line);margin-bottom:12px}
.points li:last-child{border:none}

.shipping{left:98px;top:626px;width:718px;height:80px;border-radius:4px;background:linear-gradient(var(--orange),var(--orange-deep));color:#fff}
.shipping-main{position:absolute;left:32px;top:8px;font-size:44px;letter-spacing:-1.5px;font-weight:400;white-space:nowrap}
.shipping-main b{font-weight:700}
.shipping-note{position:absolute;right:46px;top:59px;font-size:12px;text-transform:uppercase}

.menu{left:96px;top:717px;width:182px;height:268px;background:#fff;border:1px solid var(--line);border-radius:3px}
.menu-title{background:linear-gradient(var(--orange),var(--orange-deep));color:#fff;font-weight:600;font-size:20px;letter-spacing:-0.5px;height:40px;padding:8px 25px}
.menu ul{list-style:none;padding:0 20px 0 27px}
.menu li{font-style:italic;font-size:14px;font-weight:600;color:#555;height:32.5px;line-height:32.5px;border-bottom:1px solid #e6e6e6}
.menu li:last-child{border:none}
.menu li.current{color:var(--orange-deep)}

.product{left:290px;top:717px;width:526px;height:268px;background:#fff;border:1px solid var(--line);border-radius:3px}
.product-image{position:absolute;left:45px;top:38px;width:160px;height:140px;border-radius:40%;background:radial-gradient(#e8f275,#bcd235)}
.info-btn{position:absolute;left:43px;top:197px;width:156px;height:42px;border-radius:4px;background:linear-gradient(var(--orange-light),var(--orange));
  color:#fff;font-style:italic;font-weight:600;font-size:22px;letter-spacing:-1px;text-align:center;line-height:42px}
.product-title{position:absolute;left:254px;top:22px;font-style:italic;font-weight:700;font-size:29px;letter-spacing:-1px;color:var(--orange)}
.product-text{position:absolute;left:254px;top:62px;width:262px;font-size:12.8px;line-height:18.3px;color:#444}

.reviews{left:96px;top:996px;width:720px;height:119px;background:#fff;border:1px solid var(--line);border-radius:3px}
.reviews h2{position:absolute;left:17px;top:14px;font-size:22px;font-weight:400;letter-spacing:-0.8px;color:var(--orange-deep)}
.reviews p{position:absolute;left:18px;top:52px;width:690px;font-size:17px;letter-spacing:-0.5px;line-height:22px;color:#333}
.reviews cite{font-style:italic;font-weight:600;color:var(--orange)}

.seal{left:848px;top:642px;width:140px;height:140px;border-radius:50%;background:var(--badge-green);opacity:.55}
.mark{left:862px;top:832px;width:124px;height:112px;border-radius:8px;background:var(--badge-teal);opacity:.35}
.award{left:866px;top:995px;width:116px;height:116px;border-radius:50%;background:var(--badge-gold);opacity:.45}

.footer{left:97px;top:1151px;display:flex;gap:17px;font-size:14.5px;font-weight:600;color:#333}
.copyright{right:93px;top:1151px;font-size:14px;color:#444}
</style>
</head>
<body>

<header>
  <div class="abs brand"><span class="brand-name">PUROVANE</span><span class="brand-dot"></span></div>
  <div class="abs contact">
    <div class="contact-line">GET IN TOUCH <b>02 5550 1234</b></div>
    <div class="contact-mail">HELLO@PUROVANE.COM.AU</div>
  </div>
</header>

<div class="abs frame"></div>

<nav class="abs nav">
  <a href="#">Home</a><a href="#">Products</a><a href="#">Order Form</a><a href="#">Data Safety</a><a href="#">Testimonials</a><a href="#">Contact Us</a>
</nav>
<div class="abs order-btn">
  <svg width="46" height="48" viewBox="0 0 46 48" fill="none" stroke="#d4dceb" stroke-width="2.5">
    <path d="M2 6h8l6 24h22l5-16H12"/><circle cx="19" cy="39" r="3.5"/><circle cx="35" cy="39" r="3.5"/>
  </svg>
  PLACE ORDER
</div>

<section class="abs hero" role="img" aria-label="White urinal with a green scented tab in the drain, on a pale tiled wall">
  <p class="abs hero-copy"><span class="b">PURO</span><span class="o">VANE</span> Toilet cystals are a dependable, safe and economical long-term odour control for toilets. They have been proven effective for over 40 years. They don't crumble or stick and they don't dissolve in water. they're made from 100% organic material and contain no soap or water soluble components. The Crystals gradually evaporate, leaving no residue to contaminate the water.</p>
  <div class="abs hero-scent">Scented</div>
  <div class="abs hero-fruit" role="img" aria-label="Lemon slice"></div>
  <div class="abs hero-tag1">BIO_DEGRADABLE</div>
  <div class="abs hero-tag2">Refresher Tabs</div>
  <div class="abs hero-product" role="img" aria-label="Green urinal tab"></div>
</section>

<ul class="abs points">
  <li>Special formula for good odour control.</li>
  <li>Unique design to promote proper flushing action</li>
  <li>Eliminate clogged drains &amp; costly repairs</li>
  <li>One size fits most urinals</li>
  <li>Long lasting fragrance</li>
  <li>Environmental Friendly</li>
  <li>Non-toxic</li>
  <li>Very Dependable</li>
</ul>

<div class="abs shipping">
  <div class="shipping-main"><b>FREE SHIPPING</b> on all orders over <b>$150</b></div>
  <div class="shipping-note">This offer is valid on all store items</div>
</div>

<aside class="abs menu">
  <div class="menu-title">Our Products</div>
  <ul>
    <li>Product Chem 01 - 02</li><li>Product Chem 03</li><li>Product Chem 04</li>
    <li class="current">Product Chem 05</li><li>Product Chem 06</li><li>Product Chem 07</li><li>Product Chem 08</li>
  </ul>
</aside>

<section class="abs product">
  <div class="product-image" role="img" aria-label="Stack of green urinal screen tabs"></div>
  <div class="info-btn">Order Info</div>
  <h2 class="product-title">Products Chem 05</h2>
  <p class="product-text">These Urinal screens contain special built-in anti-bacterial ingredients and natural fragrances. They are uniquely design to promote strong flushing with one size fitting most urinals and prevent clogging of drains and hence costly repairs. They also have a long lasting fragrance embedded in the material and are environmentally friendly and non-toxic. They will last between 30-45 days with constant use</p>
</section>

<section class="abs reviews">
  <h2>What our customers are saying about PUROVANE</h2>
  <p>We have been using purovane for over 20 year and we love the product. They are 100% organic so they are easy on the environment &nbsp;- <cite>Position, Client Name</cite></p>
</section>

<div class="abs seal" role="img" aria-label="Organic products certification badge"></div>
<div class="abs mark" role="img" aria-label="Local manufacture certification badge"></div>
<div class="abs award" role="img" aria-label="Satisfaction guarantee badge"></div>

<footer>
  <div class="abs footer"><span>Home</span><span>Products</span><span>Order Form</span><span>Data Safety</span><span>Testimonials</span><span>Contact Us</span></div>
  <div class="abs copyright">© Copyright Purovane</div>
</footer>

</body>
</html>
```